professional business card design

Business card design. Photos have been uploaded and i am open to the designer choosing which photos to use. Would like the card to be mostyly in a grey scale design with black, whites, silver & grey colours. I have added copy of our flyer as would like on the back side of card our services to be listed. Do not use any bright colurs such as blue red green or yellow. i need to be able to edit the phone number and naem in the final card design submitted.

Target Market(s)

Clients

Industry/Entity Type

earhmovibng and transport

Contact Information for Business Card

Director Name, address, email, phone number and services

Colors

Designer to choose only greyscale colors for use in the design.

Requirements
Should not have
• no yellow, red, blue or green

```html
<!DOCTYPE html>
<html lang="en">
<head>
<meta charset="utf-8">
<title>KRS Pty Ltd – Business Card</title>
<link href="https://fonts.googleapis.com/css2?family=Lato:wght@400;700;900&display=swap" rel="stylesheet">
<style>
  :root{
    --page:#2b2b2c;
    --card:#0c0c0d;
    --white:#ffffff;
    --silver:#c9c9cc;
    --grey:#8a8a8e;
    --banner:#7a7a7d;
  }
  *{box-sizing:border-box;margin:0;padding:0}
  html,body{width:1200px;height:962px;overflow:hidden}
  body{
    background:var(--page);
    font-family:'Lato',sans-serif;
    display:flex;flex-direction:column;align-items:center;justify-content:center;gap:50px;
  }
  .card{
    position:relative;width:700px;height:400px;border-radius:22px;overflow:hidden;
    background:radial-gradient(ellipse at 40% 35%,#2a2a2c 0%,var(--card) 65%);
    box-shadow:0 18px 40px rgba(0,0,0,.55);
    color:var(--white);
  }
  /* back side */
  .services-banner{
    position:absolute;left:38px;top:28px;width:300px;height:44px;
  }
  .services-banner span{
    position:absolute;left:20px;top:0;line-height:44px;font-weight:900;font-size:28px;letter-spacing:1.5px;
  }
  .service-list{
    position:absolute;left:40px;top:88px;list-style:none;
  }
  .service-list li{
    display:flex;align-items:flex-start;gap:10px;font-size:19px;line-height:24px;color:var(--white);
  }
  .service-list svg{flex:none;margin-top:5px}
  .brand-large{
    position:absolute;right:48px;top:120px;text-align:center;
  }
  .brand-large .brand-name{font-weight:900;font-size:118px;line-height:1;color:var(--silver);letter-spacing:4px}
  .brand-large .brand-suffix{font-weight:900;font-size:26px;color:var(--grey);margin-top:4px}
  /* front side */
  .contact{position:absolute;left:34px;top:26px;list-style:none}
  .contact li{display:flex;align-items:center;gap:12px;color:var(--silver);font-size:18px;line-height:30px}
  .contact .phone{font-weight:700;font-size:24px;color:var(--white)}
  .brand-small{position:absolute;left:60px;top:136px;text-align:right}
  .brand-small .brand-name{font-weight:900;font-size:64px;line-height:1;color:var(--silver);letter-spacing:3px}
  .brand-small .brand-suffix{font-weight:900;font-size:15px;line-height:20px;color:var(--grey);margin-top:2px}
  .holder{position:absolute;right:40px;top:146px;text-align:right}
  .holder-name{font-weight:900;font-size:34px;line-height:40px;color:var(--silver);letter-spacing:1px}
  .holder-role{font-size:22px;line-height:28px;color:var(--silver)}
  .truck-photo{
    position:absolute;left:0;right:0;bottom:0;height:158px;
    background:linear-gradient(90deg,#6e6a64 0%,#cfcac2 35%,#3a3a3e 60%,#8c8a86 85%,#2a2a2c 100%);
    opacity:.85;
  }
</style>
</head>
<body>

<section class="card card-back">
  <svg class="services-banner" viewBox="0 0 300 44" aria-hidden="true">
    <polygon points="0,0 270,0 300,22 270,44 0,44" fill="var(--banner)"/>
  </svg>
  <div class="services-banner"><span>OUR SERVICES</span></div>
  <ul class="service-list">
    <li><svg width="14" height="14" viewBox="0 0 14 14"><circle cx="7" cy="7" r="7" fill="#fff"/><path d="M5.5 4l3 3-3 3" stroke="#000" stroke-width="1.8" fill="none"/></svg>Over Size Loads / Hot Shot Loads</li>
    <li><svg width="14" height="14" viewBox="0 0 14 14"><circle cx="7" cy="7" r="7" fill="#fff"/><path d="M5.5 4l3 3-3 3" stroke="#000" stroke-width="1.8" fill="none"/></svg>Heavy Vehicle Recovery Services</li>
    <li><svg width="14" height="14" viewBox="0 0 14 14"><circle cx="7" cy="7" r="7" fill="#fff"/><path d="M5.5 4l3 3-3 3" stroke="#000" stroke-width="1.8" fill="none"/></svg>Poatable Water Deliveries</li>
    <li><svg width="14" height="14" viewBox="0 0 14 14"><circle cx="7" cy="7" r="7" fill="#fff"/><path d="M5.5 4l3 3-3 3" stroke="#000" stroke-width="1.8" fill="none"/></svg>Road Building / Maintenance</li>
    <li><svg width="14" height="14" viewBox="0 0 14 14"><circle cx="7" cy="7" r="7" fill="#fff"/><path d="M5.5 4l3 3-3 3" stroke="#000" stroke-width="1.8" fill="none"/></svg>Earthworks</li>
    <li><svg width="14" height="14" viewBox="0 0 14 14"><circle cx="7" cy="7" r="7" fill="#fff"/><path d="M5.5 4l3 3-3 3" stroke="#000" stroke-width="1.8" fill="none"/></svg>Sand &amp; Metal Supply &amp; Cartage</li>
    <li><svg width="14" height="14" viewBox="0 0 14 14"><circle cx="7" cy="7" r="7" fill="#fff"/><path d="M5.5 4l3 3-3 3" stroke="#000" stroke-width="1.8" fill="none"/></svg>Road Train Tippers</li>
    <li><svg width="14" height="14" viewBox="0 0 14 14"><circle cx="7" cy="7" r="7" fill="#fff"/><path d="M5.5 4l3 3-3 3" stroke="#000" stroke-width="1.8" fill="none"/></svg>Road Train Tankers</li>
    <li><svg width="14" height="14" viewBox="0 0 14 14"><circle cx="7" cy="7" r="7" fill="#fff"/><path d="M5.5 4l3 3-3 3" stroke="#000" stroke-width="1.8" fill="none"/></svg>Road Train Flat Tops</li>
    <li><svg width="14" height="14" viewBox="0 0 14 14"><circle cx="7" cy="7" r="7" fill="#fff"/><path d="M5.5 4l3 3-3 3" stroke="#000" stroke-width="1.8" fill="none"/></svg>Drop Dect Trailers</li>
    <li><svg width="14" height="14" viewBox="0 0 14 14"><circle cx="7" cy="7" r="7" fill="#fff"/><path d="M5.5 4l3 3-3 3" stroke="#000" stroke-width="1.8" fill="none"/></svg>Mine Site Accredited Equipment<br>and Operators</li>
  </ul>
  <div class="brand-large">
    <div class="brand-name">KRS</div>
    <div class="brand-suffix">Pty Ltd</div>
  </div>
</section>

<section class="card card-front">
  <ul class="contact">
    <li>
      <svg width="16" height="16" viewBox="0 0 24 24" aria-hidden="true"><path d="M6.6 10.8a15 15 0 0 0 6.6 6.6l2.2-2.2a1 1 0 0 1 1-.25 11.4 11.4 0 0 0 3.6.6 1 1 0 0 1 1 1V20a1 1 0 0 1-1 1A17 17 0 0 1 3 4a1 1 0 0 1 1-1h3.5a1 1 0 0 1 1 1c0 1.25.2 2.45.6 3.6a1 1 0 0 1-.25 1z" fill="var(--grey)"/></svg>
      <span class="phone">(123) 456-7890</span>
    </li>
    <li>
      <svg width="16" height="12" viewBox="0 0 16 12" aria-hidden="true"><rect width="16" height="12" rx="1" fill="var(--grey)"/><path d="M1 1l7 6 7-6" stroke="#111" stroke-width="1.4" fill="none"/></svg>
      <span>info@yourwebsite.com</span>
    </li>
    <li>
      <svg width="14" height="18" viewBox="0 0 14 18" aria-hidden="true"><path d="M7 0a7 7 0 0 1 7 7c0 5-7 11-7 11S0 12 0 7a7 7 0 0 1 7-7z" fill="var(--grey)"/><circle cx="7" cy="7" r="2.5" fill="#111"/></svg>
      <span>Your Address, City, State, Zip 1235</span>
    </li>
  </ul>
  <div class="brand-small">
    <div class="brand-name">KRS</div>
    <div class="brand-suffix">Pty Ltd</div>
  </div>
  <div class="holder">
    <div class="holder-name">DANIEL HART</div>
    <div class="holder-role">Director &amp; Founder</div>
  </div>
  <div class="truck-photo" role="img" aria-label="Photo of a black prime mover hauling a road train of white water tanker trailers"></div>
</section>

</body>
</html>
```